Anti Cellulite Treatment Massage Oil see link https://www.shopvelarn.example/Anti-Cellulite-Treatment-Massa

i need a packaging design for Anti Cellulite Treatment Massage Oil like this
https://www.shopvelarn.example/s/ref=nb_sb_noss?url=search-alias%3Daps&field-keywords=Anti+Cellulite+Treatment+Massage+Oil+

our company is lorba see link below https://www.shopvelarn.example/Lorba-Beauty-Herbal-Extract/dp/X77QK2M4R9/ref=sr_1_1_a_it?ie=UTF8&qid=1111111111&sr=8-1&keywords=lorba

its a 8oz / 240 ml

Target Market(s)

health & beauty

Industry/Entity Type

Massage

Font styles to use
Serif
Sans Serif
Decorative
Script

Colors

Designer to choose colors to be used in the design.

Requirements
Must have
• our logo and pump like this seller
• https://www.shopvelarn.example/Anti-Cellulite-Treatment-Massage-Oil/dp/Z52HT8W3P6/ref=sr_1_1_a_it?ie=UTF8&qid=2222222222&sr=8-1&keywords=+Anti+Cellulite+Treatment+Massage+Oil
Nice to have
• the most similar to this or even better idea from this link
Should not have
• pictures on the label

```html
<!DOCTYPE html>
<html lang="en">
<head>
<meta charset="utf-8">
<title>lorba Anti Cellulite Massage Oil – Label Designs</title>
<link rel="stylesheet" href="https://fonts.googleapis.com/css2?family=Nunito+Sans:ital,wght@0,300;0,400;0,600;1,600&family=Great+Vibes&display=swap">
<style>
  :root {
    --bg: #ececec;
    --pink: #e6a9c0;
    --ink: #2c2c2c;
    --ink-soft: #555555;
    --silver-light: #f4f4f4;
    --silver-dark: #8f8f8f;
    --white-label: #fbfbfb;
    --bronze-top: #8e7e66;
    --bronze-mid: #a39379;
    --bronze-bottom: #6f624f;
    --bronze-ink: #2f281f;
    --bronze-pink: #e9bccb;
  }
  * { box-sizing: border-box; margin: 0; padding: 0; }
  html, body { width: 1200px; height: 867px; overflow: hidden; }
  body {
    background: radial-gradient(ellipse at 50% 40%, #f6f6f6 0%, var(--bg) 75%);
    font-family: "Nunito Sans", "Helvetica Neue", Arial, sans-serif;
    position: relative;
  }
  .label-set {
    position: absolute;
    top: 228px;
    left: 250px;
    display: flex;
    gap: 40px;
  }
  .label {
    position: relative;
    width: 330px;
    height: 410px;
    overflow: hidden;
    box-shadow: 0 6px 18px rgba(0,0,0,0.12);
  }
  .label--white { background: var(--white-label); color: var(--ink); }
  .label--bronze {
    background: linear-gradient(100deg, var(--bronze-bottom) 0%, var(--bronze-mid) 35%, var(--bronze-top) 60%, var(--bronze-bottom) 100%);
    color: var(--bronze-ink);
  }
  .silver-band {
    position: absolute;
    left: 0; right: 0;
    height: 8px;
    background: linear-gradient(180deg, var(--silver-light) 0%, var(--silver-dark) 50%, var(--silver-light) 100%);
  }
  .silver-band--top { top: 0; }
  .silver-band--bottom { bottom: 0; }
  .side-copy {
    position: absolute;
    top: 40px;
    width: 30px;
    font-size: 4px;
    line-height: 6px;
    color: #9a9a9a;
  }
  .side-copy--left { left: 4px; }
  .side-copy--right { right: 4px; }
  .label--bronze .side-copy { color: #5c5142; }
  .front {
    position: absolute;
    left: 40px; right: 40px;
    top: 52px;
    text-align: center;
  }
  .brand {
    display: inline-flex;
    align-items: center;
    gap: 10px;
    font-size: 32px;
    font-weight: 400;
    color: var(--pink);
    letter-spacing: 0.5px;
  }
  .brand-dot {
    width: 28px; height: 28px;
    border-radius: 50%;
    border: 2px solid var(--pink);
  }
  .product-title {
    margin-top: 42px;
    font-size: 27px;
    font-weight: 300;
    letter-spacing: 0.5px;
  }
  .product-type {
    display: flex;
    align-items: center;
    justify-content: center;
    gap: 6px;
    margin-top: 4px;
    font-size: 20px;
    font-weight: 300;
    color: var(--ink-soft);
  }
  .product-type::before, .product-type::after {
    content: "";
    width: 34px;
    height: 1px;
    background: currentColor;
  }
  .label--bronze .product-type { color: #3f372c; }
  .tagline {
    margin-top: 10px;
    font-family: "Great Vibes", cursive;
    font-size: 17px;
    color: var(--pink);
  }
  .label--bronze .tagline { color: var(--bronze-pink); }
  .ingredients {
    margin-top: 6px;
    font-size: 8.5px;
    font-weight: 400;
    letter-spacing: 0.2px;
  }
  .description {
    margin: 30px auto 0;
    width: 200px;
    font-size: 8.5px;
    font-weight: 600;
    font-style: italic;
    line-height: 1.35;
  }
  .volume {
    margin-top: 18px;
    font-size: 11px;
    font-weight: 600;
  }
</style>
</head>
<body>
  <main class="label-set">
    <section class="label label--white" aria-label="White label, lorba Anti Cellulite Massage Oil">
      <div class="silver-band silver-band--top"></div>
      <p class="side-copy side-copy--left">Directions: apply to damp skin and massage in circular motions until absorbed.</p>
      <p class="side-copy side-copy--right">Caution: for external use only. Avoid contact with eyes. Store in a cool dry place.</p>
      <div class="front">
        <div class="brand"><span class="brand-dot"></span>lorba</div>
        <h1 class="product-title">ANTI CELLULITE</h1>
        <p class="product-type">Massage Oil</p>
        <p class="tagline">All Natural Ingredients</p>
        <p class="ingredients">GRAPE SEED OIL • EUCALYPTUS • CITRUS LEMON</p>
        <p class="description">BEST CELLULITE TREATMENT this aromatic oil helps eliminate toxins and deliver and overall feeling of wellbeing</p>
        <p class="volume">8 fl Oz / 240 ml</p>
      </div>
      <div class="silver-band silver-band--bottom"></div>
    </section>

    <section class="label label--bronze" aria-label="Bronze label, lorba Anti Cellulite Massage Oil">
      <div class="silver-band silver-band--top"></div>
      <p class="side-copy side-copy--left">Directions: apply to damp skin and massage in circular motions until absorbed.</p>
      <p class="side-copy side-copy--right">Caution: for external use only. Avoid contact with eyes. Store in a cool dry place.</p>
      <div class="front">
        <div class="brand"><span class="brand-dot"></span>lorba</div>
        <h2 class="product-title">ANTI CELLULITE</h2>
        <p class="product-type">Massage Oil</p>
        <p class="tagline">All Natural Ingredients</p>
        <p class="ingredients">GRAPE SEED OIL • EUCALYPTUS • CITRUS LEMON</p>
        <p class="description">BEST CELLULITE TREATMENT this aromatic oil helps eliminate toxins and deliver and overall feeling of wellbeing</p>
        <p class="volume">8 fl Oz / 240 ml</p>
      </div>
      <div class="silver-band silver-band--bottom"></div>
    </section>
  </main>
</body>
</html>
```